Brook Forge - Crypto Currency Miner Powered by Renewable Energy Website

We Need Web Pages Design for Website for Crypto Currency Miner

Serivices include:
Mining Rig Sales
Housing for Rigs turnkey on renewable energy grid
Cloud Mining term packages
Updates

http://www.vaultrigratings.example (Competitors sites)

Target Market(s)

Investers for Mining Rigs and terms for 1,2 or 3 years of Hash rate

Industry/Entity Type

Mining

Number of Pages Required

5+ page

Font styles to use
Sans Serif

Colors
add136
9bcb3c
606060
474747
ffc214
cadf82
fbee3e
876aae
6b449b

Requirements
Must have
• Pictures of Solar, Wind and power Factor Correction units
Nice to have
• e-commerce platform so contract terms can be purchased through website
Should not have
• Heavy construction equipment

```html
<!DOCTYPE html>
<html lang="en">
<head>
<meta charset="utf-8">
<title>Brook Forge — Renewable Crypto Mining</title>
<link rel="stylesheet" href="https://fonts.googleapis.com/css2?family=Roboto+Condensed:wght@400;700&family=Roboto:wght@400;500;700&display=swap">
<style>
:root{
  --green:#9bcb3c;
  --green-bright:#add136;
  --green-pale:#cadf82;
  --ink:#474747;
  --grey:#606060;
  --dark:#1e1e1e;
  --light:#f3f3f3;
  --white:#ffffff;
}
*{box-sizing:border-box;margin:0;padding:0}
html,body{width:1200px;height:3327px;overflow:hidden}
body{position:relative;background:var(--white);font-family:"Roboto",Arial,sans-serif;color:var(--ink)}
.heading{font-family:"Roboto Condensed","Arial Narrow",sans-serif}
section,header,footer,nav{position:absolute;left:0;width:1200px}
.abs{position:absolute}

/* top bar */
.topbar{top:0;height:40px;background:var(--green)}
.topbar-links{left:200px;top:12px;font-size:13px;font-weight:700;color:var(--white)}
.topbar-links span{margin:0 8px}
.topbar-social{right:200px;top:8px;display:flex;gap:8px}
.topbar-social i{display:block;width:24px;height:24px;border-radius:50%;background:var(--white)}

/* header */
.masthead{top:40px;height:85px;border-bottom:1px solid #e2e2e2}
.logo{left:200px;top:22px;display:flex;align-items:center;gap:10px}
.logo-dot{width:36px;height:36px;border-radius:50%;background:var(--green)}
.logo-name{font-family:"Roboto Condensed",sans-serif;font-size:24px;font-weight:700;color:var(--ink)}
.contact-item{top:22px;display:flex;gap:12px;font-size:12px;color:var(--ink)}
.contact-item .ico{width:26px;height:40px;background:#3c3c3c;display:flex;align-items:center;justify-content:center}
.contact-item b{display:block;font-size:12px;margin:3px 0 4px}
.mainnav{top:125px;height:42px;border-bottom:1px solid #e2e2e2}
.mainnav ul{position:absolute;left:200px;top:14px;list-style:none;display:flex;font-size:12px;font-weight:700;color:var(--dark)}
.mainnav li{padding:0 18px;border-right:1px solid #999;line-height:13px}
.mainnav li:first-child{padding-left:0}
.mainnav li:last-child{border:none}
.login{right:200px;top:12px;font-size:14px;color:var(--ink);display:flex;gap:8px;align-items:center}

/* hero */
.hero{top:167px;height:574px}
.hero-photo{position:absolute;inset:0;background:linear-gradient(180deg,#5fa0d8 0%,#a9cdea 38%,#4a5d86 62%,#2b3551 80%,#7a7a5a 100%)}
.hero-arrow{top:271px;width:38px;height:38px;border-radius:50%;background:var(--white);display:flex;align-items:center;justify-content:center}
.hero-box{left:400px;top:104px;width:401px;height:374px;background:rgba(155,203,60,.92);text-align:center;color:var(--white)}
.hero-box h1{font-size:70px;line-height:68px;font-weight:700;margin-top:44px}
.hero-box p{font-size:15px;color:var(--dark);margin-top:18px;line-height:21px}
.btn{display:inline-block;font-size:12px;font-weight:700;text-transform:uppercase;padding:14px 0;width:131px;text-align:center}
.btn-white{background:var(--white);color:var(--dark)}
.btn-black{background:var(--dark);color:var(--white);border:1px solid var(--white)}
.hero-btns{position:absolute;left:61px;top:281px;display:flex;gap:9px}

/* about */
.about{top:741px;height:245px;text-align:center}
.about h2{font-size:34px;font-weight:700;color:var(--dark);margin-top:67px}
.about p{width:800px;margin:20px auto 0;font-size:11.5px;line-height:22px;color:var(--ink)}

/* services */
.services{top:986px;height:567px;background:var(--light);overflow:hidden}
.services-accent{position:absolute;inset:0}
.services-rule{left:599px;top:0;width:2px;height:42px;background:var(--ink)}
.services h2{position:absolute;width:100%;top:40px;text-align:center;font-size:30px;color:var(--dark)}
.services-intro{position:absolute;width:340px;left:430px;top:84px;text-align:center;font-size:11px;line-height:19px}
.card{top:169px;height:328px;background:var(--white);text-align:center;padding:0 18px;box-shadow:0 2px 6px rgba(0,0,0,.08)}
.card svg{margin-top:48px}
.card h3{font-family:"Roboto Condensed",sans-serif;font-size:14px;font-weight:700;color:var(--dark);margin-top:22px;line-height:16px}
.card p{font-size:12px;line-height:20px;color:#888;margin-top:14px}
.card .corner{position:absolute;right:0;bottom:0;width:0;height:0;border-left:16px solid transparent;border-bottom:16px solid var(--green)}
.card-active{background:var(--green);top:166px;height:334px}
.card-active h3,.card-active p{color:var(--white)}
.card-active .corner{border-bottom-color:var(--white)}
.card-active .rule{width:40px;height:2px;background:var(--white);margin:10px auto 0}

/* try */
.try{top:1553px;height:496px}
.try h2{position:absolute;right:533px;top:72px;text-align:right;font-size:48px;line-height:56px;color:var(--dark)}
.try p{position:absolute;left:226px;top:190px;width:442px;text-align:right;font-size:15px;line-height:24px;color:#777}
.try .btn{position:absolute;left:541px;top:312px;background:var(--green);color:var(--white);width:126px;padding:12px 0}
.try-band{position:absolute;left:0;top:400px;width:1200px;height:96px;background:var(--green-bright)}
.phone{left:776px;top:89px;width:178px;height:343px;border-radius:26px;background:linear-gradient(160deg,#5aa83a,#2f7d2b)}

/* contract */
.contract{top:2049px;height:657px;background:var(--white)}
.contract-panel{left:295px;top:114px;width:612px;height:391px;background:#f6f6f6;text-align:center;border:10px solid #2a2a2a;border-radius:10px}
.contract-panel h2{font-size:30px;color:var(--dark);margin-top:40px}
.contract-panel .intro{width:340px;margin:12px auto 0;font-size:11px;line-height:17px}
.contract-panel .divider{width:400px;height:1px;background:#bbb;margin:26px auto 0}
.steps{position:absolute;left:0;top:200px;width:100%}
.step{position:absolute;top:0;width:150px;margin-left:-75px;text-align:center}
.step-wide{width:200px;margin-left:-100px}
.step .badge{width:54px;height:54px;border-radius:50%;background:var(--green);margin:0 auto;display:flex;align-items:center;justify-content:center;border:4px solid #e4e4e4}
.step b{display:block;font-size:14px;margin-top:10px;color:var(--dark)}
.step p{font-size:11.5px;line-height:17px;margin-top:6px}

/* map */
.map{top:2706px;height:443px}
.map-fill{position:absolute;inset:0;background:linear-gradient(135deg,#d8d8d8,#c4c4c4 50%,#dadada)}
.touch{left:712px;top:213px;width:288px;height:230px;background:var(--green);color:var(--white);padding:28px 30px}
.touch h4{font-size:13px;font-weight:700}
.touch .row{display:flex;gap:18px;font-size:12px;line-height:18px;margin-top:22px;align-items:flex-start}

/* footer */
.site-footer{top:3149px;height:178px}
.copy{left:200px;top:42px;font-size:12px;line-height:18px}
.footer-social{left:200px;top:98px;display:flex;gap:8px}
.footer-social i{display:block;width:22px;height:22px;background:var(--grey)}
.quick{left:388px;top:42px}
.quick h4,.newsletter h4{font-size:14px;font-weight:700;color:var(--dark)}
.quick ul{list-style:none;columns:2;column-gap:70px;font-size:12px;line-height:24px;margin-top:12px;width:260px}
.newsletter{left:708px;top:42px}
.newsletter form{display:flex;margin-top:22px}
.newsletter .field{width:204px;height:32px;background:var(--dark);color:var(--white);font-size:12px;padding:9px 10px}
.newsletter .send{width:88px;height:32px;background:var(--green);color:var(--white);font-size:12px;font-weight:700;display:flex;align-items:center;justify-content:center}
</style>
</head>
<body>

<header class="topbar">
  <div class="abs topbar-links"><span style="margin-left:0">Login</span>|<span>See Demo</span>|<span>Contact Us</span></div>
  <div class="abs topbar-social"><i></i><i></i><i></i><i></i></div>
</header>

<header class="masthead">
  <div class="abs logo"><span class="logo-dot"></span><span class="logo-name">Brook Forge</span></div>
  <div class="abs contact-item" style="left:444px">
    <span class="ico"><svg width="14" height="14" viewBox="0 0 24 24"><path d="M6 2l4 5-2 3c1 3 3 5 6 6l3-2 5 4-3 4C10 22 2 14 2 5z" fill="#fff"/></svg></span>
    <div><b>CALL :</b>+1555014927</div>
  </div>
  <div class="abs contact-item" style="left:572px">
    <span class="ico"><svg width="14" height="14" viewBox="0 0 24 24"><path d="M2 12L12 3l10 9h-3v9H5v-9z" fill="#fff"/></svg></span>
    <div><b>E-MAIL :</b>info@brookforge.example</div>
  </div>
  <div class="abs contact-item" style="left:765px">
    <span class="ico"><svg width="14" height="14" viewBox="0 0 24 24"><path d="M12 2a7 7 0 017 7c0 5-7 13-7 13S5 14 5 9a7 7 0 017-7z" fill="#fff"/><circle cx="12" cy="9" r="2.5" fill="#3c3c3c"/></svg></span>
    <div><b>LOCATION</b>Lorem Ipsum is text here industry</div>
  </div>
</header>

<nav class="mainnav">
  <ul><li>HOME</li><li>ABOUT US</li><li>SERVICES</li><li>CONTRACT TERMS</li><li>FAQ</li><li>CONTACT US</li></ul>
  <div class="abs login"><svg width="16" height="16" viewBox="0 0 24 24"><circle cx="12" cy="7" r="5" fill="#474747"/><path d="M2 23c0-6 4-9 10-9s10 3 10 9z" fill="#474747"/></svg>Login / Register</div>
</nav>

<section class="hero">
  <div class="hero-photo" role="img" aria-label="Wind turbines standing behind rows of solar panels under a blue sky"></div>
  <div class="abs hero-arrow" style="left:99px"><svg width="12" height="12" viewBox="0 0 12 12"><path d="M8 1L3 6l5 5" stroke="#474747" stroke-width="2" fill="none"/></svg></div>
  <div class="abs hero-arrow" style="left:1052px"><svg width="12" height="12" viewBox="0 0 12 12"><path d="M4 1l5 5-5 5" stroke="#474747" stroke-width="2" fill="none"/></svg></div>
  <div class="abs hero-box">
    <h1 class="heading">THE BROOK<br>FORGE</h1>
    <p>The modern IT ecosystem requires comprehensive<br>and reliable protection</p>
    <div class="hero-btns"><span class="btn btn-white">Read More</span><span class="btn btn-black">Contact Us</span></div>
  </div>
</section>

<section class="about">
  <h2 class="heading">About Us</h2>
  <p>Lorem Ipsum is simply dummy text of the printing and typesetting industry Lorem Ipsum has been the industry's standard dummy text ever since the 1500s, when an unknown printer took a galley of type and scrambled it to make a type specimen book. Lorem Ipsum is simply dummy text of the printing and typesetting industry. Lorem Ipsum has been ever since the 1500s, when an unknown.</p>
</section>

<section class="services">
  <svg class="services-accent" width="1200" height="567" viewBox="0 0 1200 567"><polygon points="1020,0 1200,0 1200,567 840,567 1000,454 1000,162 832,162" fill="#add136"/></svg>
  <div class="abs services-rule"></div>
  <h2 class="heading">Our Services</h2>
  <p class="services-intro">Lorem Ipsum is simply dummy text of the printing and typesetting industry. Lorem Ipsum has been the industry's</p>

  <div class="abs card" style="left:200px;width:226px">
    <svg width="64" height="64" viewBox="0 0 64 64" fill="none" stroke="#9bcb3c" stroke-width="3"><path d="M8 22C20 10 44 10 56 22"/><path d="M32 14v30"/><path d="M26 44h12v6H26z"/><path d="M28 50l-4 10M36 50l4 10"/></svg>
    <h3>MINING RIG SALES</h3>
    <p>Lorem Ipsum is simply dummy text of the printing and typesetting industry. Lorem Ipsum has been the industry's standard dummy text ever since the 1500s.</p>
    <span class="corner"></span>
  </div>
  <div class="abs card card-active" style="left:479px;width:242px">
    <svg width="64" height="64" viewBox="0 0 64 64" fill="none" stroke="#fff" stroke-width="3"><path d="M32 4v14M24 18h16M26 18l-8 40M38 18l8 40M14 58h36M22 38h20M20 48h24"/></svg>
    <h3>HOUSING FOR RIGS TURNKEY ON<br>RENEWABLE ENERGY GRID</h3>
    <div class="rule"></div>
    <p>Lorem Ipsum is simply dummy text of the printing and typesetting industry. Lorem Ipsum has been the industry's standard</p>
    <span class="corner"></span>
  </div>
  <div class="abs card" style="left:759px;width:239px">
    <svg width="72" height="64" viewBox="0 0 72 64" fill="none" stroke="#9bcb3c" stroke-width="3"><path d="M18 50a12 12 0 010-24 16 16 0 0131-6 12 12 0 015 30z"/><ellipse cx="38" cy="36" rx="9" ry="4" fill="#9bcb3c"/><path d="M29 36v12c0 2 4 4 9 4s9-2 9-4V36"/></svg>
    <h3>CLOUD MINING TERM PACKAGES</h3>
    <p>Lorem Ipsum is simply dummy text of the printing and typesetting industry. Lorem Ipsum has been the industry's standard dummy text ever since the 1500s.</p>
    <span class="corner"></span>
  </div>
</section>

<section class="try">
  <div class="try-band"></div>
  <h2 class="heading">Try The Brook Forge<br>Today</h2>
  <p>Lorem Ipsum is simply dummy text of the printing and typesetting industry. Lorem Ipsum has been the industry's standard dummy text ever since the 1500s, when an unknown printer took galley of type and scrambled specimen book.</p>
  <span class="btn">Contact Us</span>
  <div class="abs phone" role="img" aria-label="Smartphone showing the Brook Forge app start screen"></div>
</section>

<section class="contract">
  <div class="abs contract-panel">
    <h2 class="heading">Purchase Contract Terms</h2>
    <p class="intro">Lorem Ipsum is simply dummy text of the printing and typesetting industry. Lorem Ipsum has been the industry's</p>
    <div class="divider"></div>
    <svg class="abs" style="left:100px;top:226px" width="392" height="20" viewBox="0 0 392 20"><path d="M0 10C40 0 60 20 100 10S160 0 196 10 260 20 300 10 360 0 392 10" stroke="#999" fill="none"/></svg>
    <div class="steps">
      <div class="step" style="left:86px"><div class="badge"><svg width="24" height="20" viewBox="0 0 24 20"><rect x="1" y="3" width="22" height="15" rx="2" fill="none" stroke="#fff" stroke-width="2"/><path d="M1 8h22" stroke="#fff" stroke-width="2"/></svg></div><b>1 YEAR</b><p>Lorem Ipsum is simply dummy text of the printing &amp; typesetting industry.</p></div>
      <div class="step step-wide" style="left:296px"><div class="badge"><svg width="24" height="20" viewBox="0 0 24 20"><rect x="1" y="3" width="22" height="15" rx="2" fill="none" stroke="#fff" stroke-width="2"/><path d="M1 8h22" stroke="#fff" stroke-width="2"/></svg></div><b>2 YEAR</b><p>Lorem Ipsum is simply dummy text of the printing and typesetting industry. Lorem Ipsum has been the industry's standard</p></div>
      <div class="step" style="left:506px"><div class="badge"><svg width="24" height="20" viewBox="0 0 24 20"><rect x="1" y="3" width="22" height="15" rx="2" fill="none" stroke="#fff" stroke-width="2"/><path d="M1 8h22" stroke="#fff" stroke-width="2"/></svg></div><b>3 YEAR</b><p>Lorem Ipsum is simply dummy text of the printing &amp; typesetting industry.</p></div>
    </div>
  </div>
</section>

<section class="map">
  <div class="map-fill" role="img" aria-label="Street map of the office neighbourhood with a location marker"></div>
  <div class="abs touch">
    <h4>GET IN TOUCH</h4>
    <div class="row"><svg width="14" height="14" viewBox="0 0 24 24"><path d="M6 2l4 5-2 3c1 3 3 5 6 6l3-2 5 4-3 4C10 22 2 14 2 5z" fill="#fff"/></svg><span>+1555014927</span></div>
    <div class="row"><svg width="14" height="16" viewBox="0 0 24 24"><path d="M12 2a7 7 0 017 7c0 5-7 13-7 13S5 14 5 9a7 7 0 017-7z" fill="#fff"/></svg><span>Lorem Ipsum is simply dummy text<br>of the printing industry.</span></div>
    <div class="row"><svg width="14" height="12" viewBox="0 0 24 18"><rect x="1" y="1" width="22" height="16" fill="none" stroke="#fff" stroke-width="2"/><path d="M1 1l11 9 11-9" stroke="#fff" stroke-width="2" fill="none"/></svg><span>info@brookforge.example</span></div>
  </div>
</section>

<footer class="site-footer">
  <div class="abs copy">© the brook forge 2018<br>All Rights Reserved</div>
  <div class="abs footer-social"><i></i><i></i><i></i><i></i></div>
  <div class="abs quick">
    <h4>Quick Links</h4>
    <ul><li>Home</li><li>About Us</li><li>Services</li><li>Contract Terms</li><li>FAQ</li><li>Contact Us</li></ul>
  </div>
  <div class="abs newsletter">
    <h4>Sign Up To Our Newsletter</h4>
    <form><span class="field">Enter Your E-mail</span><span class="send">SIGN UP</span></form>
  </div>
</footer>

</body>
</html>
```